Fernwick

We require a professional design for a Cosmetic Surgery college. We have just submitted the request for our new logo which will be used on this card. We are the leaders in our field of education in Australia and this should be reflected in the quality of the card. People want to come and study with us because we are so outstanding in the field. Studying with us provides credibility, quality and courage.
Updates

Project Deadline Extended
Reason: Require updated logo to be used in design

Target Market(s)

25 - 40 year old professional women primarily from a medical background wanting to continue study in the cosmetic medical field, western speaking countries. The course average cost is 17k AU for 16 weeks.

Industry/Entity Type

Education

Requirements
Must have
• Must us the logo that is currently under design by this company.
Nice to have
• A medical twist very subtle would be nice possilbly rod of Asclepius.
Should not have
• Should not look old, we are dealing with modern medical concepts.
The logo that is being redesigned 3d silver, the attached logo is the old one.

```html
<!DOCTYPE html>
<html lang="en">
<head>
<meta charset="utf-8">
<title>Fernwick – Business Card</title>
<link href="https://fonts.googleapis.com/css2?family=Open+Sans:wght@400;600;700&display=swap" rel="stylesheet">
<style>
  :root {
    --bg: #e4e2de;
    --card: #f4f4f4;
    --teal: #0f6e8c;
    --ink: #222222;
    --muted: #444444;
    --silver: #9a9a9a;
    --faint: #e6e6e6;
  }
  * { box-sizing: border-box; margin: 0; padding: 0; }
  html, body { width: 1200px; height: 900px; overflow: hidden; }
  body {
    background: var(--bg);
    font-family: "Open Sans", Arial, sans-serif;
    position: relative;
  }
  .card {
    position: absolute;
    top: 298px;
    width: 530px;
    height: 303px;
    background: var(--card);
    box-shadow: 0 6px 18px rgba(0,0,0,0.18);
    overflow: hidden;
  }
  .card--front { left: 50px; }
  .card--back { left: 620px; }

  /* Front */
  .brand { position: absolute; left: 34px; top: 30px; }
  .brand__name {
    display: flex; align-items: center; gap: 8px;
    font-weight: 700; font-size: 30px; letter-spacing: 1px;
    color: var(--teal); line-height: 1;
  }
  .brand__dot { width: 20px; height: 20px; border-radius: 50%; background: var(--teal); }
  .brand__tagline {
    margin-top: 4px; margin-left: 28px;
    font-size: 7.5px; letter-spacing: 2.4px; color: var(--teal); text-transform: uppercase;
  }
  .decor {
    position: absolute; left: 40px; top: 90px;
    width: 170px; height: 170px; border-radius: 50%;
    background: radial-gradient(circle, var(--faint) 0%, rgba(230,230,230,0.4) 70%, transparent 71%);
  }
  .contact { position: absolute; left: 292px; top: 116px; color: var(--muted); font-size: 12px; line-height: 1.55; }
  .contact__name { font-weight: 700; font-size: 15px; color: var(--ink); letter-spacing: 0.3px; }
  .contact__role { color: var(--teal); font-size: 11px; margin-bottom: 8px; }
  .contact__line { display: flex; align-items: center; gap: 8px; }
  .contact__icon { width: 12px; height: 12px; margin-left: -22px; margin-right: 2px; }
  .contact__line--icon { margin-left: 22px; }
  .footer-band {
    position: absolute; left: 0; bottom: 0; width: 250px; height: 40px;
    background: var(--teal); border-top-right-radius: 26px;
    color: #fff; font-size: 12.5px; letter-spacing: 0.4px;
    display: flex; align-items: center; padding-left: 30px;
  }
  .footer-rule { position: absolute; left: 0; right: 0; bottom: 0; height: 8px; background: var(--teal); }

  /* Back */
  .emblem {
    position: absolute; left: 40px; top: 34px; width: 60px; height: 150px;
    border-radius: 30px;
    background: linear-gradient(180deg, #d6d6d6, #ececec);
  }
  .back-brand { position: absolute; left: 150px; top: 104px; }
  .back-brand .brand__name { color: var(--silver); font-size: 40px; gap: 10px; }
  .back-brand .brand__dot { width: 26px; height: 26px; background: var(--silver); }
  .back-brand .brand__tagline { color: var(--silver); font-size: 9px; margin-left: 36px; letter-spacing: 3px; }
</style>
</head>
<body>
  <section class="card card--front" aria-label="Business card front">
    <div class="brand">
      <div class="brand__name"><span class="brand__dot"></span>FERNWICK</div>
      <div class="brand__tagline">Medical Aesthetics Education</div>
    </div>
    <div class="decor" role="img" aria-label="Faint brand emblem decoration"></div>
    <div class="contact">
      <div class="contact__name">Owen Marsh</div>
      <div class="contact__role">physician</div>
      <div>PO Box 218</div>
      <div>Harlow Bay, RI 02914</div>
      <div class="contact__line contact__line--icon">
        <svg class="contact__icon" viewBox="0 0 12 12" aria-hidden="true"><path d="M2 4c0-1.5 1.8-2.5 4-2.5s4 1 4 2.5l-1.5.6-.5-1.2H4L3.5 4.6zM3 6h6l1 4H2z" fill="var(--teal)"/></svg>
        <span>+49 (0) 151 20475318</span>
      </div>
      <div class="contact__line contact__line--icon">
        <svg class="contact__icon" viewBox="0 0 12 12" aria-hidden="true"><rect x="1" y="2.5" width="10" height="7" fill="none" stroke="var(--teal)" stroke-width="1.2"/><path d="M1 2.5l5 4 5-4" fill="none" stroke="var(--teal)" stroke-width="1.2"/></svg>
        <span>owen@fernwick.com</span>
      </div>
    </div>
    <div class="footer-rule"></div>
    <div class="footer-band">www.fernwick.com</div>
  </section>

  <section class="card card--back" aria-label="Business card back">
    <div class="emblem" role="img" aria-label="Subtle silver rod of Asclepius illustration"></div>
    <div class="brand back-brand">
      <div class="brand__name"><span class="brand__dot"></span>FERNWICK</div>
      <div class="brand__tagline">Medical Aesthetics Education</div>
    </div>
  </section>
</body>
</html>
```